Drywall plastering business card design

Attached is my new logo and a picture of my current business card. I would like my new logo incorporated in to the business card and also my website which is:
www.ridgecrestwallfinishers.co.nz
Industry/Entity Type
Business
Contact Information for Business Card
I would like a picture of my van and my new logo on my new business card. See attached files for pictures of my old business card, van picture and logo.
Colors
0555a3
ffffff
Requirements
Must have
- New logo, Van, contact info

```html
<!DOCTYPE html>
<html lang="en">
<head>
<meta charset="utf-8">
<title>Ridgecrest Wall Finishers – Business Card</title>
<link rel="stylesheet" href="https://fonts.googleapis.com/css2?family=Exo+2:wght@400;500;700&display=swap">
<style>
  :root{
    --page:#e9e9ea;
    --card-white:#f7f7f8;
    --panel:#38393b;
    --brand-blue:#0555a3;
    --accent-blue:#1a7fd4;
    --text-light:#ffffff;
    --text-soft:#d9d9db;
  }
  *{margin:0;padding:0;box-sizing:border-box}
  html,body{width:1200px;height:899px;overflow:hidden;background:var(--page)}
  body{display:flex;align-items:center;justify-content:center;font-family:"Exo 2",sans-serif}
  .card{position:relative;width:1000px;height:571px;border-radius:42px;overflow:hidden;
    background:var(--card-white);box-shadow:0 14px 40px rgba(0,0,0,.18)}
  .card-shapes{position:absolute;inset:0;width:100%;height:100%}
  .brand{position:absolute;left:60px;top:200px;width:340px;display:flex;align-items:center;gap:16px;
    color:var(--brand-blue);font-weight:700;line-height:1.02}
  .brand-dot{flex:none;width:26px;height:26px;border-radius:50%;background:var(--brand-blue)}
  .brand-name{font-size:44px;text-transform:uppercase;letter-spacing:.5px}
  .identity{position:absolute;left:560px;top:70px;color:var(--text-light)}
  .person-name{font-size:30px;font-weight:500;letter-spacing:2px}
  .person-role{font-size:19px;color:var(--text-soft);margin-top:6px;margin-left:112px}
  .address{position:absolute;left:560px;top:185px;color:var(--text-light);font-size:22px;line-height:36px;letter-spacing:.5px}
  .contacts{position:absolute;right:58px;top:300px;list-style:none;color:var(--text-light);font-size:20px}
  .contacts li{display:flex;align-items:center;justify-content:flex-end;gap:14px;height:42px;letter-spacing:1px}
  .contacts .small{font-size:18px;letter-spacing:.3px}
  .contacts svg{width:22px;height:22px;flex:none;fill:none;stroke:var(--text-light);stroke-width:1.8}
</style>
</head>
<body>
<main class="card">
  <svg class="card-shapes" viewBox="0 0 1000 571" aria-hidden="true">
    <path fill="var(--accent-blue)" d="M428,0 H452 C472,250 382,470 252,571 H222 C360,470 448,250 428,0 Z"/>
    <path fill="var(--panel)" d="M452,0 H1000 V571 H252 C382,470 472,250 452,0 Z"/>
  </svg>

  <div class="brand">
    <span class="brand-dot"></span>
    <span class="brand-name">Ridgecrest<br>Wall<br>Finishers</span>
  </div>

  <header class="identity">
    <h1 class="person-name">MARK ELLISON</h1>
    <p class="person-role">Managing Director</p>
  </header>

  <address class="address" style="font-style:normal">
    14 Kowhai Lane,<br>Arrowtown 9302
  </address>

  <ul class="contacts">
    <li>021 482 7730
      <svg viewBox="0 0 24 24"><path d="M5 3h4l2 5-2.5 1.5a11 11 0 0 0 6 6L16 13l5 2v4a2 2 0 0 1-2 2A17 17 0 0 1 3 5a2 2 0 0 1 2-2z"/></svg>
    </li>
    <li>021 482 7731
      <svg viewBox="0 0 24 24"><rect x="7" y="2" width="10" height="20" rx="2"/><path d="M11 18h2"/></svg>
    </li>
    <li>03 442 7730
      <svg viewBox="0 0 24 24"><rect x="4" y="9" width="16" height="12" rx="1"/><path d="M7 9V3h8l2 2v4M8 13h2M12 13h2M8 17h2M12 17h2"/></svg>
    </li>
    <li class="small">mark@ridgecrestwall.co.nz
      <svg viewBox="0 0 24 24"><rect x="3" y="5" width="18" height="14" rx="1"/><path d="M3 6l9 7 9-7"/></svg>
    </li>
    <li class="small">www.ridgecrestwallfinishers.co.nz
      <svg viewBox="0 0 24 24"><circle cx="12" cy="12" r="9"/><path d="M3 12h18M12 3c3 3 3 15 0 18M12 3c-3 3-3 15 0 18"/></svg>
    </li>
  </ul>
</main>
</body>
</html>
```